Business card design needed

We need something on the back that allows the customer to get five stamps then the sixth visit they get 25 dollars to spend.
Industry/Entity Type
Business
Contact Information for Business Card
Quality meat,value for money,spit roast hire, wholesale pubs clubs,cater for bbqs.marlow lane butchery 217 marlow lane.64739204.

```html
<!DOCTYPE html>
<html lang="en">
<head>
<meta charset="utf-8">
<title>Marlow Lane Butchery – Business Card</title>
<link rel="stylesheet" href="https://fonts.googleapis.com/css2?family=Arimo:wght@700&family=Open+Sans:ital,wght@0,400;0,600;1,700&display=swap">
<style>
  :root {
    --backdrop: #e4e4e4;
    --card-white: #ffffff;
    --brown: #5f3716;
    --brown-text: #5a2e12;
    --cream: #ffffff;
    --tan: #c99c6e;
  }
  * { box-sizing: border-box; margin: 0; padding: 0; }
  html, body { width: 1200px; height: 900px; overflow: hidden; }
  body { background: var(--backdrop); position: relative; font-family: "Open Sans", sans-serif; }

  .card {
    position: absolute;
    width: 617px;
    height: 338px;
    border-radius: 14px;
    overflow: hidden;
    box-shadow: 0 3px 8px rgba(0,0,0,0.25);
  }
  .card--front { left: 103px; top: 72px; background: var(--card-white); }
  .card--back  { left: 483px; top: 482px; background: var(--brown); }

  .card__band { position: absolute; left: 0; right: 0; bottom: 0; height: 12px; }
  .card--front .card__band { background: var(--brown); }
  .card--back .card__band { background: var(--card-white); }

  .brand {
    position: absolute;
    left: 0; right: 0;
    top: 78px;
    display: flex;
    align-items: center;
    justify-content: center;
    gap: 14px;
    font-family: "Open Sans", sans-serif;
    font-weight: 600;
    font-size: 34px;
    letter-spacing: 0.5px;
  }
  .brand__dot { width: 22px; height: 22px; border-radius: 50%; }
  .card--front .brand { color: var(--brown-text); }
  .card--front .brand__dot { background: var(--tan); }
  .card--back .brand { color: var(--cream); top: 66px; }
  .card--back .brand__dot { background: var(--tan); }

  .contact {
    position: absolute;
    display: flex;
    align-items: center;
    gap: 6px;
    font-family: "Arimo", sans-serif;
    font-weight: 700;
    font-size: 16.5px;
    color: var(--brown-text);
  }
  .contact__icon { width: 31px; height: 31px; flex: none; }
  .contact--address { left: 100px; top: 194px; }
  .contact--phone { left: 350px; top: 194px; }
  .contact--email { left: 122px; top: 245px; letter-spacing: 1px; }
  .contact-divider {
    position: absolute;
    left: 306px; top: 186px;
    width: 2px; height: 46px;
    background: var(--brown-text);
  }

  .services {
    position: absolute;
    left: 0; right: 0; top: 144px;
    text-align: center;
    color: var(--cream);
    font-size: 14.5px;
    line-height: 26px;
  }

  .offer {
    position: absolute;
    left: 80px; top: 224px;
    width: 460px;
    color: var(--cream);
    font-style: italic;
    font-weight: 700;
    font-size: 20px;
    line-height: 32px;
  }
  .offer__line { display: block; padding-left: 60px; }
  .offer__line--second { padding-left: 60px; }
  .offer__mark { position: absolute; width: 52px; height: 36px; }
  .offer__mark--open { left: 0; top: 4px; }
  .offer__mark--close { left: 388px; top: 44px; }
</style>
</head>
<body>

  <section class="card card--front" aria-label="Business card front">
    <div class="brand"><span class="brand__dot"></span>Marlow Lane Butchery</div>

    <div class="contact contact--address">
      <svg class="contact__icon" viewBox="0 0 32 32" aria-hidden="true">
        <circle cx="16" cy="16" r="16" fill="#5f3716"/>
        <path d="M8 16.5 16 9l8 7.5h-2.5V24h-4v-5h-3v5h-4v-7.5z" fill="#fff"/>
      </svg>
      <span>217 marlow lane</span>
    </div>
    <div class="contact-divider"></div>
    <div class="contact contact--phone">
      <svg class="contact__icon" viewBox="0 0 32 32" aria-hidden="true">
        <circle cx="16" cy="16" r="16" fill="#5f3716"/>
        <path d="M11 8.5c.8-.5 1.7-.3 2.1.5l1.6 3c.4.7.2 1.5-.4 2l-1.1.9c.9 2.1 2.4 3.6 4.5 4.6l.9-1.1c.5-.6 1.3-.8 2-.4l3 1.6c.8.4 1 1.3.5 2.1l-1 1.6c-.6.9-1.7 1.3-2.7 1-5.3-1.5-9.4-5.6-10.9-10.9-.3-1 .1-2.1 1-2.7z" fill="#fff"/>
      </svg>
      <span>02-6473-9204</span>
    </div>
    <div class="contact contact--email">
      <svg class="contact__icon" viewBox="0 0 32 32" aria-hidden="true">
        <circle cx="16" cy="16" r="16" fill="#5f3716"/>
        <rect x="8" y="10.5" width="16" height="11" fill="#fff"/>
        <path d="M8 10.5l8 6.5 8-6.5" fill="none" stroke="#5f3716" stroke-width="1.4"/>
      </svg>
      <span>marlowlnbutchery@mailbox.com</span>
    </div>

    <div class="card__band"></div>
  </section>

  <section class="card card--back" aria-label="Business card back">
    <div class="brand"><span class="brand__dot"></span>Marlow Lane Butchery</div>

    <p class="services">
      Quality meat |&nbsp; value for money |&nbsp; spit roast hire |&nbsp; wholesale pubs clubs<br>
      cater for barbeques
    </p>

    <p class="offer">
      <svg class="offer__mark offer__mark--open" viewBox="0 0 52 36" aria-hidden="true">
        <path d="M4 34c-3-8 0-22 14-30l3 4c-6 4-8 9-7 12 5 0 8 4 8 8 0 4-4 7-9 7-5 0-8-1-9-1zM28 34c-3-8 0-22 14-30l3 4c-6 4-8 9-7 12 5 0 8 4 8 8 0 4-4 7-9 7-5 0-8-1-9-1z" fill="#fff"/>
      </svg>
      <span class="offer__line">spend $50 or more to recieve a stamp</span>
      <span class="offer__line offer__line--second">and recieve $25 off your 6th visit.</span>
      <svg class="offer__mark offer__mark--close" viewBox="0 0 52 36" aria-hidden="true">
        <path d="M48 2c3 8 0 22-14 30l-3-4c6-4 8-9 7-12-5 0-8-4-8-8 0-4 4-7 9-7 5 0 8 1 9 1zM24 2c3 8 0 22-14 30l-3-4c6-4 8-9 7-12-5 0-8-4-8-8 0-4 4-7 9-7 5 0 8 1 9 1z" fill="#fff"/>
      </svg>
    </p>

    <div class="card__band"></div>
  </section>

</body>
</html>
```